Website design in Wordpress for Golf Simulator Center

We are opening a new golf simulator center in Copenhagen, and need a website design. We are using wordpress, and our site is https://fernway-putt.dk
We will need a design for the frontpage, and a design for subpages (which we will be reusing for all subpages).
Logo is as seen on the site, and our base color scheme is leaf green.
As text, take the text on the current website, or put some placeholder text in english.
Should be responsive and look good on both desktop and mobile.
Target Market(s)
Male, 18-60, golf players
Coding
Coded - Design and coding required
Number of Pages Required
2 page
Font styles to use
Look and feel

```html
<!DOCTYPE html>
<html lang="en">
<head>
<meta charset="utf-8">
<title>Fernway Putt – Golf for everyone</title>
<link href="https://fonts.googleapis.com/css2?family=Montserrat:wght@400;500;600;700;800&display=swap" rel="stylesheet">
<style>
:root{
  --green:#0aa384;
  --green-dark:#088f73;
  --mint:#e5f7f2;
  --mint-bright:#bff2e3;
  --ink:#0b0b0b;
  --text:#333;
  --white:#fff;
  --navy:#1c2b4a;
}
*{margin:0;padding:0;box-sizing:border-box}
html,body{width:1200px;height:4066px;overflow:hidden}
body{font-family:'Montserrat',sans-serif;color:var(--text);background:var(--white);position:relative}
.abs{position:absolute}
.photo{position:absolute}
.btn{position:absolute;display:flex;align-items:center;justify-content:center;font-size:11px;font-weight:700;text-transform:uppercase;letter-spacing:.2px}
.btn-green{background:var(--green);color:var(--white)}
.btn-white{background:var(--white);color:var(--ink)}
.label{position:absolute;font-size:17px;font-weight:500}
.label.green{color:var(--green)}
.label .rule{display:block;width:50px;height:2px;background:var(--green);margin-top:6px}
.h-xl{position:absolute;font-weight:800;line-height:1.05}
.copy{position:absolute;font-size:11px;line-height:1.8}
.g{color:var(--green)}
.lt{color:var(--mint-bright)}

/* header */
.hero{position:absolute;left:0;top:0;width:1200px;height:490px;background:linear-gradient(100deg,#050807 0%,#18241b 45%,#2f4a2a 70%,#101410 100%)}
.logo{position:absolute;font-weight:800;font-size:24px;letter-spacing:.5px;display:flex;align-items:center;gap:8px}
.logo .mark{width:18px;height:18px;display:inline-block}
.nav{position:absolute;left:546px;top:34px;display:flex;gap:12px;font-size:14px;font-weight:700;color:var(--white)}
.book{left:979px;top:29px;width:99px;height:27px}
.arrow{position:absolute;width:33px;height:33px;border-radius:50%;background:var(--green);display:flex;align-items:center;justify-content:center}

/* cards */
.card{position:absolute;width:313px;height:423px;border:1px solid var(--green);background:var(--white);overflow:hidden}
.card h3{position:absolute;left:28px;top:27px;font-size:20px;font-weight:600;line-height:1.05;color:var(--green)}
.card p{position:absolute;left:28px;top:86px;width:250px;font-size:11px;line-height:1.8;color:var(--text)}
.card .btn{left:28px;top:159px;width:92px;height:26px}
.card .photo{left:0;top:213px;width:313px;height:210px}
.card.featured{background:var(--green)}
.card.featured .photo{top:0;height:194px}
.card.featured h3{top:234px;color:var(--white)}
.card.featured p{top:292px;color:var(--white)}
.card.featured .btn{top:365px}

/* accordion */
.accordion{position:absolute;left:212px;top:2285px;width:776px;background:var(--green);color:var(--white)}
.acc-head{height:33px;display:flex;align-items:center;padding:0 18px;font-size:11px;font-weight:600;gap:14px;position:relative}
.acc-head .chev{position:absolute;right:18px;font-size:12px}
.acc-body{background:var(--white);color:#555;font-size:10px;line-height:1.8;padding:10px 12px 8px;height:58px}
.acc-item{height:35px;display:flex;align-items:center;padding:0 18px;gap:14px;font-size:11px;font-weight:600;position:relative}
.acc-item .chev{position:absolute;right:18px}

/* form */
.field-label{position:absolute;left:122px;font-size:11px;font-weight:600;color:var(--ink)}
.field{position:absolute;left:122px;width:464px;border:1px solid var(--green);background:var(--white)}
.send{left:122px;top:3554px;width:227px;height:26px;background:var(--ink);color:var(--white);text-transform:none;font-weight:500}

/* footer */
.footer{position:absolute;left:0;top:3636px;width:1200px;height:430px;background:var(--green);color:var(--white)}
.foot-h{position:absolute;font-size:18px;font-weight:700}
.foot-t{position:absolute;font-size:12px;line-height:1.95;font-weight:500}
.social{list-style:none}
.social li{display:flex;align-items:center;gap:7px;font-size:11px;line-height:1.75}
.social li i{width:8px;height:8px;border-radius:50%;background:var(--white);display:inline-block}
</style>
</head>
<body>

<!-- HERO -->
<section class="hero" role="img" aria-label="Golfer swinging in a dark indoor simulator bay facing a large projected golf course screen"></section>
<svg class="abs" style="left:0;top:380px" width="1200" height="120" viewBox="0 0 1200 120" preserveAspectRatio="none">
  <path d="M0 90 C150 30 300 40 460 80 C620 120 720 110 880 70 C1000 40 1100 30 1200 55 L1200 120 L0 120 Z" fill="var(--mint)"/>
</svg>
<div class="abs" style="left:0;top:498px;width:1200px;height:460px;background:var(--mint)"></div>
<svg class="abs" style="left:0;top:900px" width="1200" height="120" viewBox="0 0 1200 120" preserveAspectRatio="none">
  <path d="M0 100 C200 60 380 50 560 70 C740 90 860 30 1000 20 C1100 14 1160 30 1200 40 L1200 0 L0 0 Z" fill="var(--mint)"/>
</svg>

<div class="logo" style="left:120px;top:30px;color:var(--green)"><span class="mark" style="background:var(--green)"></span>FERNWAY PUTT</div>
<nav class="nav"><span>HOME</span><span>ABOUT US</span><span>OUR SERVICES</span><span>BLOGS</span><span>CONTACT US</span></nav>
<div class="btn btn-green book">BOOK NOW</div>

<h1 class="h-xl" style="left:115px;top:122px;font-size:57px;color:var(--white)">Golf for<br><span class="lt">everyone</span></h1>
<p class="copy" style="left:115px;top:246px;width:480px;color:var(--white);font-weight:500">Beginner or pro – everyone can play on our simulators. If you don't have golf equipment yourself, you can borrow it free of charge directly from us. Bring friends, family or colleagues and hit some shots.</p>
<div class="btn btn-green" style="left:115px;top:319px;width:110px;height:26px">GET A QUOTE</div>
<div class="arrow" style="left:1004px;top:302px"><svg width="16" height="16" viewBox="0 0 16 16"><path d="M13 8H4M8 3L3 8l5 5" stroke="#111" stroke-width="2.6" fill="none"/></svg></div>
<div class="arrow" style="left:1047px;top:302px"><svg width="16" height="16" viewBox="0 0 16 16"><path d="M3 8h9M8 3l5 5-5 5" stroke="#111" stroke-width="2.6" fill="none"/></svg></div>

<!-- ABOUT -->
<div class="label green" style="left:115px;top:567px">ABOUT US</div>
<h2 class="h-xl" style="left:115px;top:605px;font-size:47px;color:var(--ink)">Who we are!</h2>
<p class="copy" style="left:115px;top:670px;width:475px">Beginner or pro – everyone can play on our simulators. If you don't have golf equipment yourself, you can borrow it free of charge directly from us. Bring friends, family or colleagues and hit some shots. Indoor golf center with 6 simulators in Nordhavn. Play golf indoors in all weathers, whether driving range or a full 18-hole round. Our high-tech simulators from FlightTrace capture the ball from your stroke with high precision. See all data on the big screen.</p>
<div class="btn btn-green" style="left:115px;top:802px;width:152px;height:26px">SEE MORE ABOUT US</div>
<div class="photo" style="left:606px;top:570px;width:479px;height:245px;background:linear-gradient(180deg,#1a1a16 0%,#6b6a3e 35%,#4b6b2a 60%,#223d16 100%)" role="img" aria-label="Golfer addressing the ball in front of a simulator screen showing a sunset course"></div>

<!-- CARDS -->
<article class="card" style="left:115px;top:1061px">
  <h3>State-of-the-art<br>technology</h3>
  <p>Our high-tech simulators from FlightTrace capture the ball from your stroke with high precision. See all data on the big screen.</p>
  <div class="btn btn-green">SEE MORE</div>
  <div class="photo" style="background:linear-gradient(120deg,#0e1a14 0%,#1e3d2c 45%,#4d8a5b 65%,#0c1510 100%)" role="img" aria-label="Player swinging in a dark simulator room"></div>
</article>
<article class="card featured" style="left:444px;top:1061px">
  <div class="photo" style="left:0;width:313px;background:linear-gradient(180deg,#1a1a16 0%,#6b6a3e 35%,#4b6b2a 60%,#223d16 100%)" role="img" aria-label="Golfer at a simulator bay with a bag of clubs"></div>
  <h3>State-of-the-art<br>technology</h3>
  <p>Our high-tech simulators from FlightTrace capture the ball from your stroke with high precision. See all data on the big screen.</p>
  <div class="btn btn-white">SEE MORE</div>
</article>
<article class="card" style="left:770px;top:1061px">
  <h3>State-of-the-art<br>technology</h3>
  <p>Our high-tech simulators from FlightTrace capture the ball from your stroke with high precision. See all data on the big screen.</p>
  <div class="btn btn-green">SEE MORE</div>
  <div class="photo" style="background:linear-gradient(180deg,#2a5d9a 0%,#3e7fb5 40%,#4f8a3a 65%,#1c2a14 100%)" role="img" aria-label="Two players in a bright simulator bay"></div>
</article>

<!-- TRAINING -->
<section class="abs" style="left:0;top:1533px;width:1200px;height:521px;background:var(--green)"></section>
<div class="label" style="left:115px;top:1676px;color:var(--white)">Golf Training</div>
<h2 class="h-xl" style="left:115px;top:1713px;font-size:47px;color:var(--white)">Take Your Game<br>to the <span class="lt">Next</span> Level</h2>
<p class="copy" style="left:115px;top:1828px;width:440px;color:var(--white)">We are not just a regular golf club. We are a friendly community of experienced enthusiasts and professionals</p>
<div class="btn btn-white" style="left:115px;top:1882px;width:92px;height:26px">SEE MORE</div>
<div class="photo" style="left:726px;top:1574px;width:359px;height:242px;background:linear-gradient(160deg,#7ea84a 0%,#5c8a2c 50%,#3d6620 100%)" role="img" aria-label="Golf ball resting at the edge of the cup on a green"></div>
<div class="photo" style="left:606px;top:1773px;width:359px;height:239px;background:linear-gradient(180deg,#111 0%,#2a5d9a 30%,#4f8a3a 60%,#1a2a12 100%);border:1px solid var(--green)" role="img" aria-label="Two players in a simulator bay"></div>

<!-- CONDITIONS -->
<div class="label green" style="left:0;width:1200px;text-align:center;top:2101px">Conditions</div>
<h2 class="h-xl" style="left:0;width:1200px;text-align:center;top:2138px;font-size:52px;color:var(--ink)">Conditions for membership</h2>
<p class="copy" style="left:260px;width:680px;text-align:center;top:2200px">Fernway Putt offers different memberships. These conditions apply to all types of membership. Memberships are also subject to our normal trading conditions and personal data policy . Prices and conditions for membership can be changed by Fernway Putt at any time.</p>
<div class="accordion">
  <div class="acc-head"><span>—</span>Payment<span class="chev">⌄</span></div>
  <div class="acc-body">Lorem ipsum dolor sit amet, consectetur adipisicing elit. Optio, neque qui velit. Magni dolorum quidem ipsam eligendi, totam, facilis laudantium cum accusamus ullam voluptatibus commodi numquam, error, est. Ea, consequatur.</div>
  <div class="acc-item"><span>+</span>Revocation/termination<span class="chev">›</span></div>
  <div class="acc-item"><span>+</span>Use of membership benefits<span class="chev">›</span></div>
  <div class="acc-item"><span>+</span>Key tag<span class="chev">›</span></div>
  <div class="acc-item"><span>+</span>Guests<span class="chev">›</span></div>
</div>

<!-- MEMBERSHIP -->
<div class="abs" style="left:420px;top:2561px;width:780px;height:534px;background:var(--mint)"></div>
<div class="photo" style="left:122px;top:2708px;width:224px;height:336px;background:linear-gradient(170deg,#8a7a60 0%,#5c6a36 40%,#3b5a1e 100%)" role="img" aria-label="Hand placing a golf ball on a tee"></div>
<div class="photo" style="left:362px;top:2602px;width:224px;height:336px;background:linear-gradient(170deg,#1e2a10 0%,#5a7a2a 45%,#6f8f36 100%)" role="img" aria-label="Fingers setting a golf ball on turf"></div>
<div class="label" style="left:606px;top:2687px;color:var(--ink)">Indoor Golf Membership</div>
<h2 class="h-xl" style="left:606px;top:2724px;font-size:47px;color:var(--ink)"><span class="g">It's Our</span> Indoor<br>Golf <span class="g">Membership</span><br><span class="g">Club</span></h2>
<p class="copy" style="left:606px;top:2884px;width:440px">We are not just a regular golf club. We are a friendly community of experienced enthusiasts and professionals</p>
<div class="btn btn-green" style="left:606px;top:2940px;width:92px;height:25px">SEE MORE</div>

<!-- CONTACT -->
<div class="label" style="left:122px;top:3142px;color:var(--ink)">Indoor Golf Membership<span class="rule"></span></div>
<h2 class="h-xl" style="left:122px;top:3181px;font-size:47px;color:var(--ink)"><span class="g">Need a</span> help?<br><span class="g">Don't</span> worry <span class="g">just</span><br><span class="g">contact us</span></h2>
<div class="field-label" style="top:3341px">Name</div>
<div class="field" style="top:3360px;height:30px"></div>
<div class="field-label" style="top:3401px">Email</div>
<div class="field" style="top:3419px;height:31px"></div>
<div class="field-label" style="top:3461px">Message</div>
<div class="field" style="top:3478px;height:67px"></div>
<div class="btn send">Send</div>
<div class="photo" style="left:726px;top:3136px;width:359px;height:238px;background:linear-gradient(160deg,#7ea84a 0%,#5c8a2c 50%,#3d6620 100%)" role="img" aria-label="Golf ball resting at the edge of the cup on a green"></div>
<div class="photo" style="left:606px;top:3333px;width:359px;height:239px;background:linear-gradient(180deg,#111 0%,#2a5d9a 30%,#4f8a3a 60%,#1a2a12 100%)" role="img" aria-label="Two players in a simulator bay"></div>

<!-- FOOTER -->
<footer class="footer">
  <h2 class="h-xl" style="left:115px;top:88px;font-size:38px;color:var(--white);line-height:1.02">We conduct <span class="lt">indoor golf</span> lessons &amp;<br>tournaments, training</h2>
  <div class="logo" style="left:853px;top:100px;color:var(--navy);font-size:26px"><span class="mark" style="background:var(--navy);width:22px;height:22px"></span>FERNWAY PUTT</div>

  <div class="foot-h" style="left:115px;top:193px">Address</div>
  <div class="foot-t" style="left:115px;top:230px">Denmark <span style="display:inline-block;width:68px;height:1px;background:var(--white);vertical-align:middle;margin-left:12px"></span><br>Fernway Putt ApS, Lindevej 14,<br>2150 Nordhavn, Denmark</div>

  <div class="foot-h" style="left:461px;top:200px">Say Hello</div>
  <div class="foot-t" style="left:461px;top:234px;text-decoration:underline">info@fernway-putt.dk</div>
  <div class="foot-t" style="left:461px;top:274px">+45 20 11 40 58</div>

  <div class="foot-h" style="left:655px;top:200px">Say Hello</div>
  <ul class="social abs" style="left:655px;top:234px">
    <li><i></i>Facebook</li><li><i></i>Google</li><li><i></i>Twitter</li><li><i></i>Instagram</li><li><i></i>LinkedIn</li>
  </ul>

  <div class="foot-h" style="left:849px;top:200px">Newsletter</div>
  <div class="foot-t" style="left:857px;top:236px;font-size:10px;opacity:.85">Enter Your Email</div>
  <svg class="abs" style="left:1045px;top:240px" width="10" height="12" viewBox="0 0 10 12"><path d="M1 1l8 5-4 1-1 4z" fill="var(--white)"/></svg>
  <div class="abs" style="left:849px;top:262px;width:228px;height:1px;background:var(--white)"></div>
  <div class="foot-t" style="left:849px;top:278px;font-size:10px;display:flex;align-items:center;gap:8px"><svg width="10" height="10" viewBox="0 0 10 10"><rect width="10" height="10" fill="var(--white)"/><path d="M2 5l2 2 4-4" stroke="var(--green)" stroke-width="1.6" fill="none"/></svg>I agree to the Privacy Policy.</div>

  <div class="abs" style="left:115px;top:351px;width:970px;height:1px;background:rgba(255,255,255,.7)"></div>
  <div class="foot-t" style="left:115px;top:366px">FernwayPutt © 2023. All Rights Reserved.</div>
</footer>

</body>
</html>
```